Kleine Werbebroschüre für Bauunternehmen (Deckblatt plus  1. und 2. Seite)
Kleine Werbebroschüre für Bauunternehmen (Deckblatt plus 1. und 2. Seite)
Zielgruppe
Private Bauherren, Familien
Aufgabenstellung
Guten Tag zusammen,
wir benötigen einen klein Broschüre für ein Bauunternehmen, welche angelehnt werden kann an das Design unserer Internetseite www.kolmar-steinbau.de. Die Broschüre soll nur aus einem Deckblatt und dann beim Aufklappen aus einer ersten und zweiten Seite bestehen, die Rückseite kann frei bleiben bzw. hier genügt ein kleiner farblicher Balken mit z. B. unseren Kontaktinformationen. Die Bilder, Logos und Texte, welche verarbeitet werden sollen, laden wir gerne über das Portal hoch. Zur ganz groben Orientierung haben wir ein Word Dokument angelegt und hochgeladen, das Hausbild auf dem Deckblatt muss nicht, aber kann eingebaut werden, es muss sich halt gut in das Gesamtbild einfügen. Wir wünschen uns eine modernes, hochwertiges und vertrauenserweckendes Design, die Website soll nur zur Orientierung gelten und Eure Kreativität nicht einschränken. Wir sind für alle Vorschläge offen. Wenn es fragen gibt, sind wir jederzeit für Euch ansprechbar.
Wir freuen uns auf Eure Vorschläge.
Lukas

```html
<!DOCTYPE html>
<html lang="de">
<head>
<meta charset="utf-8">
<title>Kolmar Steinbau – Broschüre</title>
<link href="https://fonts.googleapis.com/css2?family=Cabin:wght@400;500;600&display=swap" rel="stylesheet">
<style>
:root{
  --heading:#4b5a7c;
  --rule:#4f5d7e;
  --text:#2f3033;
  --accent:#1f9a52;
  --paper:#f4f4f0;
  --shade:#dcdedf;
  --seal:#c9ced8;
}
*{margin:0;padding:0;box-sizing:border-box}
html,body{width:848px;height:1200px;overflow:hidden}
body{
  font-family:"Cabin",sans-serif;
  color:var(--text);
  background:radial-gradient(ellipse at 20% 95%,var(--shade) 0%,transparent 55%),
             linear-gradient(180deg,#f7f7f3 0%,var(--paper) 60%,#eceeee 100%);
  position:relative;
}
.abs{position:absolute}
.h{font-weight:500;color:var(--heading);letter-spacing:.4px;font-size:25px;line-height:30px}
.h1{left:47px;top:26px}
.h2{left:47px}
.rule{left:23px;width:780px;height:2px;background:var(--rule)}
.copy{font-size:11.5px;line-height:13.7px;letter-spacing:.2px}
.copy p+p{margin-top:13.7px}
.green{color:var(--accent);font-weight:600}
.photo{left:39px;top:144px;width:188px;height:130px;border:1px solid #8a8a8a;
  background:linear-gradient(135deg,#e9edf1 0%,#c9b5a0 45%,#d8cfc4 70%,#f3f4f5 100%)}
.seal{left:674px;top:95px;width:86px;height:86px;border-radius:8px;background:var(--seal)}
.icon{width:39px;height:33px;left:762px}
.check{left:58px;width:46px;height:44px}
.point{left:112px;font-size:11.5px;line-height:13.7px;letter-spacing:.2px;color:var(--heading);white-space:nowrap}
.url{left:614px;top:1162px;font-size:16px;color:var(--heading);letter-spacing:.3px}
</style>
</head>
<body>

<h1 class="abs h h1">Sie suchen ein Traumhaus für Ihre Familie ?</h1>
<div class="abs rule" style="top:56px"></div>

<div class="abs copy" style="left:39px;top:76px;width:740px">
  <p>Kolmar Steinbau ist spezialisiert auf den Bau von Massivhäusern - deutschlandweit. Wir bauen für Sie solide Stein auf Stein und auf<br>Wunsch nach den Standards für ein förderfähiges FBK-Effizienzhaus (Förderbank für Klimabau).</p>
  <p>Zur Freude der Umwelt und Ihrer Brieftasche.</p>
</div>

<div class="abs photo" role="img" aria-label="Foto einer lachenden Familie vor einem hellen Haus"></div>

<div class="abs seal" role="img" aria-label="Platz für ein Prüfsiegel"></div>

<div class="abs copy" style="left:241px;top:145px;width:430px">
  <p>Zur unabhängigen und objektiven Bauüberwachung arbeiten wir mit der<br><span class="green">CERTANO-Bauüberwachung</span> zusammen. Die Zertifizierung durch die <span class="green">CERTANO</span><br>garantiert höchste Immobilienqualität und Sicherheit und ist in jedem unserer<br>Angebote bereits standardmäßig inklusive -<br>zu Ihrer Sicherheit.</p>
  <p>Von der Erstberatung bis hin zur schlüsselfertigen Übergabe Ihres Massivhauses<br>bieten wir als Totalübernehmer ein komplettes Leistungsportfolio für unsere<br>Kunden.</p>
</div>

<div class="abs copy" style="left:39px;top:283px;width:770px">
  <p>Mit unseren Fachberatern, Bauingenieuren, Architekten sowie unseren angeschlossenen Handwerks-Meisterbetrieben gewährleisten wir<br>unseren Kunden <span class="green">CERTANO</span> zertifizierte Massivhaus-Qualität.</p>
</div>

<h2 class="abs h h2" style="top:348px">Warum massiv bauen ?</h2>
<svg class="abs icon" style="top:341px" viewBox="0 0 39 33" fill="none" stroke="var(--rule)" stroke-width="2.4">
  <path d="M2 14L19.5 2L37 14M4 13V31H35V17"/><text x="15" y="26" font-size="15" fill="var(--rule)" stroke="none" font-family="Cabin,sans-serif">?</text>
</svg>
<div class="abs rule" style="top:377px"></div>
<div class="abs copy" style="left:41px;top:398px;width:750px">
  <p>In erster Linie heißt massiv Bauen, wertbeständig und nachhaltig zu bauen.</p>
  <p>Mittel- und langfristig gesehen hat ein Massivhaus einen wesentlich höheren Wiederverkaufswert als ein Fertighaus.<br>Die Nutzungsdauer eines Hauses in Massivbauweise wird mit ca. 100 Jahren beziffert.</p>
  <p>Dies wird beim Massivhausbau durch immer günstigere Konditionen der Banken und Versicherungen honoriert.<br>Eine individuelle Planung ist bei Massivhäusern problemlos möglich.</p>
</div>

<h2 class="abs h h2" style="top:516px">Bauzeit</h2>
<svg class="abs icon" style="top:509px" viewBox="0 0 39 33" fill="none" stroke="var(--rule)" stroke-width="2.4">
  <path d="M2 14L19.5 2L37 14M4 13V31H35V17"/><circle cx="19.5" cy="20" r="6.5" stroke-width="1.6"/><path d="M19.5 20L23 17" stroke-width="1.6"/>
</svg>
<div class="abs rule" style="top:546px"></div>
<div class="abs copy" style="left:36px;top:565px;width:760px">
  <p>Von Fertighausanbietern wird meist mit einer sehr kurzen Errichtungszeit des Rohbaus geworben, was aber nur einen relativ kleinen<br>Zeitabschnitt der Gesamtbauzeit betrifft.</p>
  <p>Eine kurze Montagezeit verschleiert oft die lange Vorlaufzeit der Fertighaushersteller für die Produktion bis zur Montage.<br>Deswegen spielt ein Zeitvorteil gegenüber der Massivbauweise keine Rolle.</p>
</div>

<h2 class="abs h h2" style="top:674px">Raumklima</h2>
<svg class="abs icon" style="top:667px" viewBox="0 0 39 33" fill="none" stroke="var(--rule)" stroke-width="2.4">
  <path d="M2 14L19.5 2L37 14M4 13V31H35V17"/><path d="M18 12V22" stroke-width="2"/><circle cx="18" cy="24.5" r="2.5" stroke-width="1.6"/>
</svg>
<div class="abs rule" style="top:703px"></div>
<div class="abs copy" style="left:36px;top:724px;width:770px">
  <p>Ein Massivhaus verfügt über eine sehr gute Wärmespeicherfähigkeit.<br>Dadurch, dass das Mauerwerk Wärme, sowohl von außen als auch von innen absorbiert, herrschen zu jeder Jahreszeit angenehme<br>Temperaturen im Inneren.</p>
  <p>Außerdem sind massive Wände in der Lage die Feuchtigkeit zu regulieren, was ein gesundes Raumklima im ganzen Haus garantiert.</p>
</div>

<h2 class="abs h h2" style="top:828px">Wärmeschutzverhalten</h2>
<svg class="abs icon" style="top:821px" viewBox="0 0 39 33" fill="none" stroke="var(--rule)" stroke-width="2.4">
  <path d="M2 14L19.5 2L37 14M4 13V31H35V17"/><path d="M14 26C11 22 17 19 14 15M19.5 26C16.5 22 22.5 19 19.5 15M25 26C22 22 28 19 25 15" stroke-width="1.5"/>
</svg>
<div class="abs rule" style="top:856px"></div>
<div class="abs copy" style="left:36px;top:877px;width:720px">
  <p>Die heutigen Baustoffe, die bei der Herstellung des massiven Außenmauerwerks verwendet werden, kommen denen der<br>Holzrahmenbauweise in vielen Punkten zuvor:</p>
</div>

<svg class="abs check" style="top:925px" viewBox="0 0 46 44" fill="none" stroke="var(--rule)">
  <rect x="2" y="11" width="30" height="30" stroke-width="3.5"/><path d="M9 24L18 36L43 2" stroke-width="6" stroke-linejoin="round"/>
</svg>
<div class="abs point" style="top:920px">In einem Haus in Holzrahmenbauweise lebt man quasi in einer Plastiktüte um der<br>Energieeinsparverordnung zu genügen.<br>Das Außenmauerwerk eines Massivhauses hingegen ist diffusionsoffen, dadurch wird die Feuchtigkeit<br>die als Dampf oder Kondensat durch Waschen, Kochen oder Duschen anfällt ausgeglichen.<br>Es entsteht ein deutlich merkbares gesünderes Raumklima ohne Gefahr der Schimmelbildung.</div>

<svg class="abs check" style="top:1006px" viewBox="0 0 46 44" fill="none" stroke="var(--rule)">
  <rect x="2" y="11" width="30" height="30" stroke-width="3.5"/><path d="M9 24L18 36L43 2" stroke-width="6" stroke-linejoin="round"/>
</svg>
<div class="abs point" style="top:1010px">In den massiven Innenwänden wird Wärme im Winter gespeichert. So muss nach einem<br>Lüftungsvorgang nicht die ganze Raumluft neu aufgeheizt werden. Im Sommer wird unnötige Wärme<br>gespeichert und es bleibt im Raum kühler.</div>

<svg class="abs check" style="top:1071px" viewBox="0 0 46 44" fill="none" stroke="var(--rule)">
  <rect x="2" y="11" width="30" height="30" stroke-width="3.5"/><path d="M9 24L18 36L43 2" stroke-width="6" stroke-linejoin="round"/>
</svg>
<div class="abs point" style="top:1076px">Anbieter von Fertighäusern versuchen meist mit dem guten Wärmedämmverhalten ihrer<br>Außenwandkonstruktion zu punkten. Außenwände sind aber nur an ca. 15% des gesamten<br>Energieverlustes eines Wohnhauses beteiligt.</div>

<div class="abs url">www.kolmar-steinbau.de</div>

</body>
</html>
```